Designer Instructions – Updated Referral Program Flyer

(Based on the mock-up in “Brief Layout and Instructions.pdf”)

OVERALL STYLE + LAYOUT

Maintain the same general layout, structure, and flow as the mock-up flyer (front and back).

This is an update of an older flyer, not a full redesign — keep the same sections, proportions, and overall visual feel, but with cleaner, more modern design improvements.

The final flyer should look clean, bold, professional, and high-impact, geared toward realtors, property managers, and contractors who refer work.

FRONT SIDE INSTRUCTIONS
1. Header Section

Remove the Tallow Ridge Builders logo from the top banner.
(Shown on page 1 of the PDF)

2. Main Headline

Keep the same three-line structure:
EARN
UNLIMITED
CASH

Center it, maximize impact, and increase the font size of CASH so all three words match in importance.

Make the headline bold, clean, and the main focal point.

3. Cash Incentive Box

Keep the "$500 minimum OR 10% per referral" box, but upgrade the graphics to look sharper and more modern.

Ensure the wording matches exactly what’s in the mock-up.

4. Premier Partner Program Ribbon

Clean up and modernize the "PREMIER PARTNER PROGRAM" bar while keeping the same position and structure.

Ensure the checkmark badge remains crisp and professional.

5. Supporting Icons Section

Keep the four icons/benefit boxes (Guaranteed Payout, Free Evaluations, Affordable Solutions, Industry Leaders) in the same order.

Update the icons to cleaner, more modern styles — but maintain the same meanings.

Improve alignment and spacing for sharper visual consistency.

6. Remove Icons in Contact Area

At the bottom (“CALL TEXT OR BOOK ONLINE 555-014-2796 TallowRidgeBuilders.example”), remove the phone and internet icons, as noted on page 2 of the PDF.

7. Replace All Images

I (Darnell) will provide all updated stock images separately via email.

Replace the flood/water-damage imagery and roof leak with the new images I send.

Keep image placement and proportions the same as the mock-up.

BACK SIDE INSTRUCTIONS
1. Header Image + “REFER / EARN” Section

Maintain the same large split-image layout (“The more you refer, the more you earn”).

Replace all background imagery with the new assets I will send.

Keep the CASH FLOW image section but modernize the type and spacing.

2. “HOW IT WORKS” Section

Preserve the three-column layout:

Refer Flood, Water & Mold Damage

We Take Care of Everything (evaluations/insurance)

Get Paid to Share

Update images, tighten spacing, and use modern iconography.

3. Remove Phone/Internet Icons

Same as the front side — remove small communication icons and keep only the text/number/URL.

4. Bottom Contact Bar

Keep the blue bar, same wording, same layout — just modernize the style if needed for clarity.

5. Replace All Back-Side Images

Again, I will email you the image assets.

Keep the layout EXACT — just update with higher-quality photos and improved design.

TEXT CONTENT (Keep as-is unless spacing adjustments needed)

All text shown in the PDF should remain exactly the same unless spacing or visual balance requires minor adjustments.
Example from page 3:

“REFER FLOOD, MOLD & CONSTRUCTION JOBS”

“We Schedule a Free Estimate. If Approved, You Get Paid.”

“Everybody Benefits From Referrals”

Everything stays, just refreshed and visually improved.

DESIGN GOALS

Flyer should look high-end and trustworthy, not salesy.

Consistent color theme: blues, whites, yellows, same palette as original.

Use bold, modern fonts with strong readability.

Ensure all headlines pop and all benefit boxes are clean, well-aligned, and evenly spaced.

The final result should feel like a premium referral program flyer for a top-tier restoration/remodel company.

FILES I WILL PROVIDE

I will send the designer:

All replacement stock photos

Any updated logos (if needed)

Original high-resolution version of the mock-up (if available)

Any additional icons preferred

0054AA
0677BA
7BADD7
CADEEF
E8F1F8

• Designer Instructions – Updated Referral Program Flyer (Based on the mock-up in “Brief Layout and Instructions.pdf”) OVERALL STYLE + LAYOUT Maintain the same general layout, structure, and flow as the mock-up flyer (front and back). This is an update of an older flyer, not a full redesign — keep the same sections, proportions, and overall visual feel, but with cleaner, more modern design improvements. The final flyer should look clean, bold, professional, and high-impact, geared toward realtors, property managers, and contractors who refer work. FRONT SIDE INSTRUCTIONS 1. Header Section Remove the Tallow Ridge Builders logo from the top banner. (Shown on page 1 of the PDF) 2. Main Headline Keep the same three-line structure: EARN UNLIMITED CASH Center it, maximize impact, and increase the font size of CASH so all three words match in importance. Make the headline bold, clean, and the main focal point. 3. Cash Incentive Box Keep the "$500 minimum OR 10% per referral" box, but upgrade the graphics to look sharper and more modern. Ensure the wording matches exactly what’s in the mock-up. 4. Premier Partner Program Ribbon Clean up and modernize the "PREMIER PARTNER PROGRAM" bar while keeping the same position and structure. Ensure the checkmark badge remains crisp and professional. 5. Supporting Icons Section Keep the four icons/benefit boxes (Guaranteed Payout, Free Evaluations, Affordable Solutions, Industry Leaders) in the same order. Update the icons to cleaner, more modern styles — but maintain the same meanings. Improve alignment and spacing for sharper visual consistency. 6. Remove Icons in Contact Area At the bottom (“CALL TEXT OR BOOK ONLINE 555-014-2796 TallowRidgeBuilders.example”), remove the phone and internet icons, as noted on page 2 of the PDF. 7. Replace All Images I (Darnell) will provide all updated stock images separately via email. Replace the flood/water-damage imagery and roof leak with the new images I send. Keep image placement and proportions the same as the mock-up. BACK SIDE INSTRUCTIONS 1. Header Image + “REFER / EARN” Section Maintain the same large split-image layout (“The more you refer, the more you earn”). Replace all background imagery with the new assets I will send. Keep the CASH FLOW image section but modernize the type and spacing. 2. “HOW IT WORKS” Section Preserve the three-column layout: Refer Flood, Water & Mold Damage We Take Care of Everything (evaluations/insurance) Get Paid to Share Update images, tighten spacing, and use modern iconography. 3. Remove Phone/Internet Icons Same as the front side — remove small communication icons and keep only the text/number/URL. 4. Bottom Contact Bar Keep the blue bar, same wording, same layout — just modernize the style if needed for clarity. 5. Replace All Back-Side Images Again, I will email you the image assets. Keep the layout EXACT — just update with higher-quality photos and improved design. TEXT CONTENT (Keep as-is unless spacing adjustments needed) All text shown in the PDF should remain exactly the same unless spacing or visual balance requires minor adjustments. Example from page 3: “REFER FLOOD, MOLD & CONSTRUCTION JOBS” “We Schedule a Free Estimate. If Approved, You Get Paid.” “Everybody Benefits From Referrals” Everything stays, just refreshed and visually improved. DESIGN GOALS Flyer should look high-end and trustworthy, not salesy. Consistent color theme: blues, whites, yellows, same palette as original. Use bold, modern fonts with strong readability. Ensure all headlines pop and all benefit boxes are clean, well-aligned, and evenly spaced. The final result should feel like a premium referral program flyer for a top-tier restoration/remodel company. FILES I WILL PROVIDE I will send the designer: All replacement stock photos Any updated logos (if needed) Original high-resolution version of the mock-up (if available) Any additional icons preferred

```html
<!DOCTYPE html>
<html lang="en">
<head>
<meta charset="utf-8">
<title>Referral Program Flyer – Front and Back</title>
<link href="https://fonts.googleapis.com/css2?family=Poppins:wght@400;500;600;700;800;900&family=Anton&display=swap" rel="stylesheet">
<style>
:root{
  --stage:#2e2e2e;
  --navy:#0c1630;
  --blue:#1b3f8c;
  --blue-mid:#23499a;
  --yellow:#ffd51c;
  --yellow-hi:#f5e92a;
  --orange:#f7861e;
  --white:#ffffff;
  --ink:#0e1326;
  --paper:#f2f3f5;
}
*{box-sizing:border-box;margin:0;padding:0}
html,body{width:1200px;height:914px;overflow:hidden}
body{background:var(--stage);font-family:'Poppins',sans-serif;position:relative}
.flyer{position:absolute;top:96px;width:468px;height:723px;background:var(--white);overflow:hidden}
.flyer--front{left:106px}
.flyer--back{left:626px}
.abs{position:absolute}
.photo{position:absolute}

/* FRONT */
.front-photo{left:180px;top:0;width:288px;height:263px;background:linear-gradient(160deg,#c9d6dc,#9fb7c4 45%,#6d8796);clip-path:polygon(0 0,100% 0,100% 100%,26% 100%,10% 10%)}
.hero-panel{left:0;top:26px;width:300px;height:155px;background:linear-gradient(90deg,var(--navy),var(--blue));clip-path:polygon(0 0,253px 0,296px 100%,0 100%)}
.headline{left:22px;top:38px;font-weight:800;font-size:43px;line-height:43px;letter-spacing:0;white-space:nowrap}
.headline .y{color:var(--yellow)}
.headline .w{color:var(--white)}
.payout-bar{left:0;top:181px;width:300px;height:30px;background:linear-gradient(90deg,var(--blue),var(--blue-mid));clip-path:polygon(0 0,256px 0,270px 100%,0 100%)}
.payout-bar span{position:absolute;left:23px;top:2px;color:var(--white);font-weight:700;font-size:18px;white-space:nowrap}
.payout-tip{left:240px;top:181px;width:70px;height:30px;background:var(--orange);clip-path:polygon(0 0,40% 0,70% 100%,30% 100%)}
.incentive{left:0;top:211px;width:300px;height:52px;background:linear-gradient(90deg,var(--yellow-hi),var(--yellow) 40%,var(--orange));clip-path:polygon(0 0,270px 0,300px 100%,0 100%)}
.min{left:23px;top:214px;font-weight:700;color:var(--ink);line-height:1}
.min small{display:block;font-size:13px;font-weight:600}
.min b{font-size:25px;font-weight:800}
.or-badge{left:97px;top:216px;width:40px;height:40px}
.pct{left:141px;top:216px;color:var(--ink);line-height:1;white-space:nowrap}
.pct b{font-size:21px;font-weight:800}
.pct span{font-size:19px;font-weight:500}
.pct small{display:block;font-size:11px;font-weight:700;margin-top:2px}
.estimates{left:0;top:263px;width:468px;height:66px;background:linear-gradient(90deg,var(--white),var(--paper))}
.estimates h2{position:absolute;left:23px;top:3px;color:var(--blue);font-weight:800;font-size:31px;line-height:36px;white-space:nowrap}
.estimates p{position:absolute;left:23px;top:37px;color:var(--ink);font-size:19px;font-weight:500;white-space:nowrap}
.afford{left:0;top:329px;width:262px;height:68px;background:linear-gradient(90deg,var(--yellow),var(--orange));clip-path:polygon(0 0,234px 0,254px 100%,0 100%)}
.afford h3{position:absolute;left:23px;top:3px;color:var(--white);font-weight:800;font-size:28px;line-height:29px;white-space:nowrap}
.afford-notch{left:232px;top:329px;width:30px;height:16px;background:var(--navy);clip-path:polygon(0 0,60% 0,100% 100%,0 100%)}
.afford-list{left:236px;top:345px;width:232px;height:49px;background:var(--blue);clip-path:polygon(0 0,100% 0,100% 100%,16px 100%)}
.afford-checks{position:absolute;left:268px;top:348px;list-style:none}
.afford-checks li{display:flex;align-items:center;gap:7px;color:var(--white);font-size:12.5px;font-weight:500;height:21px;line-height:21px;white-space:nowrap}
.afford-checks svg{flex:none}
.inspect-photo{left:0;top:404px;width:468px;height:161px;background:linear-gradient(100deg,#8fbde6 0%,#b9c9d4 35%,#7e8a5e 70%,#5d6e45 100%)}
.leaders-bg{left:0;top:565px;width:468px;height:34px;background:var(--navy)}
.leaders-left{left:0;top:565px;width:250px;height:34px;background:var(--blue);clip-path:polygon(0 0,236px 0,250px 100%,0 100%)}
.leaders{left:0;top:565px;width:468px;height:34px}
.leaders b{position:absolute;left:25px;top:3px;color:var(--white);font-size:19.5px;font-weight:800;white-space:nowrap}
.leaders span{position:absolute;left:252px;top:7px;color:var(--white);font-size:14px;font-weight:500;white-space:nowrap}
.guarantee{left:0;top:599px;width:468px;height:54px;background:linear-gradient(90deg,var(--white),#e7e9ec)}
.guarantee p{position:absolute;left:23px;top:3px;font-size:33px;font-weight:600;color:var(--ink);white-space:nowrap}
.guarantee em{font-style:normal;font-weight:800;background:linear-gradient(90deg,var(--yellow),var(--orange));-webkit-background-clip:text;background-clip:text;color:transparent}
.contact{left:0;top:653px;width:468px;height:47px;background:var(--navy)}
.contact-left{left:0;top:653px;width:190px;height:47px;background:var(--blue);clip-path:polygon(0 0,176px 0,190px 100%,0 100%)}
.contact-label{left:22px;top:656px;color:var(--white);font-weight:700;font-size:15.5px;line-height:19px;white-space:nowrap}
.contact-info{left:198px;top:657px;color:var(--white);font-weight:700;line-height:20px;white-space:nowrap}
.contact-info .phone{font-size:17px;letter-spacing:2.4px}
.contact-info .web{font-size:12.5px;letter-spacing:.5px;font-weight:600}

/* BACK */
.money-photo{left:0;top:26px;width:290px;height:287px;background:linear-gradient(135deg,#d8dccf,#a7ae98 50%,#7c8a74);clip-path:polygon(0 0,196px 0,290px 100%,0 100%)}
.cashflow-tiles{left:8px;top:108px;width:200px;height:118px;background:linear-gradient(180deg,#9ee0e0,#7fcfd2);opacity:.85;border-radius:4px}
.back-hero{left:196px;top:26px;width:272px;height:287px;background:linear-gradient(160deg,var(--blue) 0%,var(--navy) 60%);clip-path:polygon(0 0,100% 0,100% 100%,92px 100%)}
.slogan{left:291px;top:68px;width:140px;text-align:center;font-family:'Anton',sans-serif;line-height:1;text-transform:uppercase}
.slogan .sm{display:block;color:var(--white);font-size:27px;letter-spacing:-.3px;white-space:nowrap}
.slogan .lg{display:block;font-size:60px;background:linear-gradient(180deg,var(--yellow) 40%,var(--orange));-webkit-background-clip:text;background-clip:text;color:transparent;letter-spacing:-1px}
.card-photo{top:334px;width:128px;height:115px;clip-path:polygon(0 0,82% 0,100% 16%,100% 100%,0 100%);border:1px solid var(--orange)}
.card-photo.flood{left:26px;background:linear-gradient(180deg,#8f9490,#5a5f5a 55%,#3c403b)}
.card-photo.estimate{left:170px;background:linear-gradient(100deg,#8fbde6,#c7ccc2 55%,#8c9a70)}
.card-photo.sign{left:314px;background:linear-gradient(180deg,#7fb2e0,#d7e6f2)}
.card{top:456px;width:128px;height:85px;background:var(--navy);padding:7px 0 0 10px}
.card h4{color:var(--yellow);font-weight:700;font-size:10px;line-height:13px;text-transform:uppercase;white-space:nowrap}
.card ul{list-style:none;position:absolute;left:10px;top:52px}
.card li{display:flex;align-items:center;gap:5px;color:var(--white);font-size:6.8px;height:16px;font-weight:500;white-space:nowrap}
.c1{left:26px}.c2{left:170px}.c3{left:314px}
.refer-blue{left:140px;top:556px;width:328px;height:88px;background:linear-gradient(90deg,var(--navy),var(--blue));clip-path:polygon(0 0,100% 0,100% 100%,32px 100%,0 0)}
.refer-orange{left:0;top:570px;width:178px;height:74px;background:linear-gradient(90deg,var(--yellow),var(--orange));clip-path:polygon(0 0,158px 0,178px 100%,0 100%)}
.refer-fold{left:140px;top:556px;width:20px;height:14px;background:var(--orange);clip-path:polygon(0 0,100% 100%,0 100%)}
.refer-label{left:21px;top:581px;font-weight:800;font-size:36px;color:var(--ink);letter-spacing:-.5px}
.refer-list{left:188px;top:566px;color:var(--white);font-weight:800;font-size:17.5px}
.refer-item{position:absolute;display:flex;align-items:center;gap:8px;white-space:nowrap}
.icon-tile{width:26px;height:26px;border-radius:4px;background:linear-gradient(180deg,var(--yellow),var(--orange));display:flex;align-items:center;justify-content:center}
</style>
</head>
<body>

<section class="flyer flyer--front">
  <div class="photo front-photo" role="img" aria-label="Kitchen with water pouring through a hole in the ceiling"></div>
  <div class="abs hero-panel"></div>
  <h1 class="abs headline"><span class="y">EARN</span><br><span class="w">UNLIMITED</span><br><span class="y">CASH</span></h1>

  <div class="abs payout-bar"><span>GUARANTEED PAYOUT</span></div>
  <div class="abs payout-tip"></div>
  <div class="abs incentive"></div>
  <div class="abs min"><small>Minimum</small><b>$500</b></div>
  <svg class="abs or-badge" viewBox="0 0 40 40" aria-hidden="true">
    <circle cx="20" cy="20" r="18" fill="#fff" stroke="#0e1326" stroke-width="1.6" stroke-dasharray="2 1.6"/>
    <text x="20" y="26" text-anchor="middle" font-family="Poppins,sans-serif" font-weight="800" font-size="16" fill="#0e1326">or</text>
  </svg>
  <div class="abs pct"><b>10%</b> <span>of</span><small>Total Invoice Paid Fast</small></div>

  <div class="abs estimates">
    <h2>FREE ESTIMATES</h2>
    <p>Fast &amp; Free Inspections &amp; Written Estimates</p>
  </div>

  <div class="abs afford"><h3>AFFORDABLE<br>SOLUTIONS</h3></div>
  <div class="abs afford-notch"></div>
  <div class="abs afford-list"></div>
  <ul class="afford-checks">
    <li><svg width="14" height="14" viewBox="0 0 14 14"><rect x="1" y="2" width="11" height="11" fill="none" stroke="#fff" stroke-width="1.3"/><path d="M3 7l3 3 7-9" fill="none" stroke="#f7861e" stroke-width="2"/></svg>Lowest Out of Pocket</li>
    <li><svg width="14" height="14" viewBox="0 0 14 14"><rect x="1" y="2" width="11" height="11" fill="none" stroke="#fff" stroke-width="1.3"/><path d="M3 7l3 3 7-9" fill="none" stroke="#f7861e" stroke-width="2"/></svg>Costs for Your Customers</li>
  </ul>

  <div class="photo inspect-photo" role="img" aria-label="Inspector holding a work estimate clipboard in front of a house"></div>

  <div class="abs leaders-bg"></div>
  <div class="abs leaders-left"></div>
  <div class="abs leaders"><b>INDUSTRY LEADERS</b><span>Licensed &amp; Certified Experts</span></div>

  <div class="abs guarantee"><p>Provide <em>100% Guarantee</em></p></div>

  <div class="abs contact"></div>
  <div class="abs contact-left"></div>
  <div class="abs contact-label">CALL, TEXT<br>OR BOOK ONLINE</div>
  <div class="abs contact-info"><div class="phone">555-014-2796</div><div class="web">www.TallowRidgeBuilders.example</div></div>
</section>

<section class="flyer flyer--back">
  <div class="photo money-photo" role="img" aria-label="Hundred dollar bills spread out"></div>
  <div class="photo cashflow-tiles" role="img" aria-label="Letter tiles spelling CASH FLOW"></div>
  <div class="abs back-hero"></div>
  <h2 class="abs slogan"><span class="sm">The more you</span><span class="lg">Refer</span><span class="sm">The more you</span><span class="lg">Earn</span></h2>

  <div class="photo card-photo flood" role="img" aria-label="Flooded room with water damage"></div>
  <div class="photo card-photo estimate" role="img" aria-label="Inspector reviewing an estimate outside a house"></div>
  <div class="photo card-photo sign" role="img" aria-label="Yellow road sign reading Get Paid to Share against the sky"></div>

  <div class="abs card c1">
    <h4>Refer Flood Mold<br>&amp; Construction<br>Jobs:</h4>
    <ul>
      <li><svg width="8" height="8" viewBox="0 0 14 14"><rect x="1" y="2" width="11" height="11" fill="none" stroke="#fff" stroke-width="1.5"/><path d="M3 7l3 3 7-9" fill="none" stroke="#f7861e" stroke-width="2.2"/></svg>It's Simple to Refer 24/7:</li>
      <li><svg width="8" height="8" viewBox="0 0 14 14"><rect x="1" y="2" width="11" height="11" fill="none" stroke="#fff" stroke-width="1.5"/><path d="M3 7l3 3 7-9" fill="none" stroke="#f7861e" stroke-width="2.2"/></svg>Call, Text or Book Online.</li>
    </ul>
  </div>
  <div class="abs card c2">
    <h4>We Take<br>Care of<br>Everything:</h4>
    <ul>
      <li><svg width="8" height="8" viewBox="0 0 14 14"><rect x="1" y="2" width="11" height="11" fill="none" stroke="#fff" stroke-width="1.5"/><path d="M3 7l3 3 7-9" fill="none" stroke="#f7861e" stroke-width="2.2"/></svg>We Schedule a Free Estimate.</li>
      <li><svg width="8" height="8" viewBox="0 0 14 14"><rect x="1" y="2" width="11" height="11" fill="none" stroke="#fff" stroke-width="1.5"/><path d="M3 7l3 3 7-9" fill="none" stroke="#f7861e" stroke-width="2.2"/></svg>If Approved, You Get Paid.</li>
    </ul>
  </div>
  <div class="abs card c3">
    <h4>Everybody<br>Benefits From<br>Referrals</h4>
    <ul>
      <li><svg width="8" height="8" viewBox="0 0 14 14"><rect x="1" y="2" width="11" height="11" fill="none" stroke="#fff" stroke-width="1.5"/><path d="M3 7l3 3 7-9" fill="none" stroke="#f7861e" stroke-width="2.2"/></svg>We Provide Expert Quality</li>
      <li><svg width="8" height="8" viewBox="0 0 14 14"><rect x="1" y="2" width="11" height="11" fill="none" stroke="#fff" stroke-width="1.5"/><path d="M3 7l3 3 7-9" fill="none" stroke="#f7861e" stroke-width="2.2"/></svg>Work for AAordable Price.</li>
    </ul>
  </div>

  <div class="abs refer-blue"></div>
  <div class="abs refer-orange"></div>
  <div class="abs refer-fold"></div>
  <div class="abs refer-label">REFER:</div>
  <div class="abs refer-list">
    <div class="refer-item" style="left:0;top:0">
      <span class="icon-tile"><svg width="16" height="16" viewBox="0 0 16 16"><path d="M2 8l6-5 6 5v3H2z" fill="#0e1326"/><path d="M1 13q2-2 3.5 0t3.5 0 3.5 0 3.5 0" fill="none" stroke="#0e1326" stroke-width="1.4"/></svg></span>FLOODS
    </div>
    <div class="refer-item" style="left:120px;top:0">
      <span class="icon-tile"><svg width="16" height="16" viewBox="0 0 16 16"><path d="M2 8l6-5 6 5" fill="none" stroke="#0e1326" stroke-width="1.6"/><path d="M4 8v6h8V8" fill="none" stroke="#0e1326" stroke-width="1.4"/><path d="M6 13l4-4M6 9l4 4" stroke="#0e1326" stroke-width="1.3"/></svg></span>REMODELS
    </div>
    <div class="refer-item" style="left:0;top:36px">
      <span class="icon-tile"><svg width="16" height="16" viewBox="0 0 16 16"><path d="M3 13l7-7" stroke="#0e1326" stroke-width="2"/><path d="M9 3l4 4-2 2-4-4z" fill="#0e1326"/></svg></span>RENOVATIONS &amp; REPAIRS
    </div>
  </div>

  <div class="abs contact"></div>
  <div class="abs contact-left"></div>
  <div class="abs contact-label">CALL, TEXT<br>OR BOOK ONLINE</div>
  <div class="abs contact-info"><div class="phone">555-014-2796</div><div class="web">www.TallowRidgeBuilders.example</div></div>
</section>

</body>
</html>
```